Flyer overhaul from current flyers

I need to have our current flyers updated with a fresher look. We also need to have a new utility and real estate flyer created that will go along with the design of the new flyer. We are looking for new pictures, new overall design, same color scheme but would like to have the flyers more airy and inviting.

Target Market(s)

decision makers in the healthcare/utilty/banking/real estate sectors

Font styles to use
Other font styles liked:
• Logo is in Bell MT

Colors
0054AA
0677BA
7BADD7
CADEEF
E8F1F8

Requirements
Must have
• Close to what is currently on the existing flyers

```html
<!DOCTYPE html>
<html lang="en">
<head>
<meta charset="utf-8">
<title>Delta Ridge Recovery – Healthcare Collections Flyers</title>
<link rel="stylesheet" href="https://fonts.googleapis.com/css2?family=Roboto:wght@400;500;700&family=Tinos:wght@700&display=swap">
<style>
  :root {
    --navy: #0b3d66;
    --deep-blue: #0054aa;
    --mid-blue: #0677ba;
    --cyan: #1aa3dc;
    --sky: #7badd7;
    --pale: #cadeef;
    --mist: #e8f1f8;
    --white: #ffffff;
    --ink: #1d2a36;
    --stage: #ededed;
  }
  * { margin: 0; padding: 0; box-sizing: border-box; }
  html, body { width: 1200px; height: 1200px; overflow: hidden; }
  body {
    background: var(--stage);
    font-family: "Roboto", Arial, sans-serif;
    position: relative;
  }
  .flyer {
    position: absolute;
    top: 245px;
    width: 547px;
    height: 709px;
    overflow: hidden;
    background: var(--navy);
    box-shadow: 0 6px 14px rgba(0,0,0,0.35);
  }
  .flyer--services { left: 34px; }
  .flyer--philosophy { left: 621px; }
  .flyer svg.shapes { position: absolute; inset: 0; }
  .abs { position: absolute; }

  /* Services flyer */
  .brand {
    left: 364px; top: 44px;
    display: flex; align-items: center; gap: 8px;
    color: var(--white); font-weight: 500; font-size: 15px;
    letter-spacing: 0.5px; text-transform: uppercase;
  }
  .brand-dot {
    width: 26px; height: 26px; border-radius: 50%;
    border: 2px solid var(--white);
  }
  .headline {
    left: 31px; top: 306px;
    color: var(--white); font-weight: 500; font-size: 33px;
    line-height: 42px; letter-spacing: 0.3px;
  }
  .tagline-bar {
    left: 0; top: 413px; width: 327px; height: 31px;
    background: var(--cyan); color: var(--white);
    font-weight: 500; font-size: 19px; line-height: 31px; padding-left: 31px;
  }
  .feature-list {
    left: 31px; top: 455px; list-style: none;
    color: var(--white); font-weight: 500; font-size: 13px; line-height: 23px;
  }
  .feature-list li::before {
    content: ""; display: inline-block; margin-right: 10px;
    border-left: 5px solid var(--white);
    border-top: 3.5px solid transparent; border-bottom: 3.5px solid transparent;
    vertical-align: 1px;
  }
  .call-label {
    left: 31px; top: 593px; color: var(--white);
    font-weight: 500; font-size: 15px;
  }
  .call-number {
    left: 31px; top: 621px; color: var(--white);
    font-weight: 500; font-size: 24px;
  }
  .web-bar {
    left: 0; top: 676px; width: 247px; height: 33px;
    background: var(--white); color: var(--navy);
    font-family: "Tinos", Georgia, serif; font-weight: 700;
    font-size: 12.5px; line-height: 33px; padding-left: 31px;
  }
  .solution-title {
    left: 335px; top: 490px; color: var(--cyan);
    font-weight: 500; font-size: 20px; line-height: 24px;
  }
  .solution-list {
    left: 351px; top: 551px; color: var(--ink);
    font-size: 10.5px; line-height: 12.8px; list-style: disc;
  }

  /* Philosophy flyer */
  .section-title {
    left: 0; width: 547px; top: 421px; text-align: center;
    color: var(--white); font-weight: 500; font-size: 40px;
  }
  .philosophy-text {
    left: 40px; width: 467px; top: 483px; text-align: center;
    color: var(--white); font-size: 11.4px; line-height: 14.8px;
  }
  .phone-panel {
    left: 34px; top: 655px; color: var(--white);
    font-weight: 500; font-size: 24px;
  }
  .contact-right {
    right: 36px; top: 636px; text-align: right; color: var(--white);
  }
  .contact-right .call-label-r {
    font-weight: 500; font-size: 15px; display: block;
    margin-right: 52px;
  }
  .contact-right .web-r {
    font-family: "Tinos", Georgia, serif; font-weight: 700;
    font-size: 12.5px; display: block; margin-top: 16px;
  }
</style>
</head>
<body>

<section class="flyer flyer--services">
  <svg class="shapes" width="547" height="709" viewBox="0 0 547 709">
    <defs>
      <linearGradient id="photoTones" x1="0" y1="0" x2="1" y2="1">
        <stop offset="0" stop-color="#1c3146"/>
        <stop offset="0.5" stop-color="#3b6b8e"/>
        <stop offset="1" stop-color="#7f9fb6"/>
      </linearGradient>
      <linearGradient id="panelBlue" x1="0" y1="0" x2="0" y2="1">
        <stop offset="0" stop-color="#0677ba"/>
        <stop offset="1" stop-color="#0b3d66"/>
      </linearGradient>
    </defs>
    <rect x="0" y="0" width="547" height="360" fill="url(#photoTones)" role="img" aria-label="Photo: two healthcare workers in scrubs reviewing information together"/>
    <path d="M0 268 C 120 250, 230 290, 310 345 L 547 300 L 547 709 L 0 709 Z" fill="url(#panelBlue)"/>
    <path d="M300 345 L 547 270 L 547 300 L 310 350 Z" fill="var(--cyan)"/>
    <path d="M310 352 L 547 305 L 547 709 L 310 709 Z" fill="var(--white)"/>
  </svg>

  <div class="abs brand"><span class="brand-dot"></span>Delta Ridge</div>

  <h1 class="abs headline">HEALTHCARE<br>COLLECTIONS</h1>
  <div class="abs tagline-bar">A Forward Thinking Approach</div>
  <ul class="abs feature-list">
    <li>A Patient Friendly, Professional Approach</li>
    <li>Live, Online Agent Chat Portal</li>
    <li>Online Debt Negotiating Tools</li>
    <li>Online Dispute Resolution Tools</li>
    <li>501(r) Compliant</li>
  </ul>
  <div class="abs call-label">CALL US AT</div>
  <div class="abs call-number">(555) 010-4782</div>
  <div class="abs web-bar">www.deltaridgerecovery.com</div>

  <h2 class="abs solution-title">An Impactful,<br>All-In-One Solution</h2>
  <ul class="abs solution-list">
    <li>Credit Report Monitoring</li>
    <li>Address/Phone Scrubbing</li>
    <li>Compliant Collection Letters</li>
    <li>Discretionary Credit Reporting</li>
    <li>Bankruptcy Claim Services</li>
    <li>Professional Skip Tracing</li>
    <li>Deceased/Probater Services</li>
    <li>Call Recording and Monitoring</li>
    <li>Legal Collection Services</li>
    <li>Customizable Collection Workflow</li>
  </ul>
</section>

<section class="flyer flyer--philosophy">
  <svg class="shapes" width="547" height="709" viewBox="0 0 547 709">
    <defs>
      <linearGradient id="homeTones" x1="0" y1="0" x2="1" y2="1">
        <stop offset="0" stop-color="#c9c2b8"/>
        <stop offset="0.55" stop-color="#a7b2b6"/>
        <stop offset="1" stop-color="#e3e0da"/>
      </linearGradient>
      <linearGradient id="panelBlue2" x1="0" y1="0" x2="0" y2="1">
        <stop offset="0" stop-color="#0677ba"/>
        <stop offset="1" stop-color="#0b3d66"/>
      </linearGradient>
    </defs>
    <rect x="0" y="0" width="547" height="405" fill="url(#homeTones)" role="img" aria-label="Photo: a nurse walking arm in arm with an elderly patient at home"/>
    <rect x="0" y="405" width="547" height="304" fill="url(#panelBlue2)"/>
    <rect x="0" y="699" width="547" height="10" fill="var(--cyan)"/>
    <path d="M0 630 L 236 630 L 272 699 L 0 699 Z" fill="var(--cyan)"/>
  </svg>

  <h2 class="abs section-title">Our Philosophy</h2>
  <p class="abs philosophy-text">Since our inception, and for over 40 years, healthcare collections have been at the center of our operation. Our philosophy is to provide consistent performance by investing in our clients accounts to ensure the maximum liquidation. By building on historically proven collection techniques and employing an ever-expanding access to data and technology, our agency has continued to improve our performance to the benefit of our clients. Our capital forward, compliance centered approach has proven to deliver consistent results to our healthcare providers.</p>

  <div class="abs phone-panel">(555) 010-4782</div>
  <div class="abs contact-right">
    <span class="call-label-r">CALL US AT</span>
    <span class="web-r">www.deltaridgerecovery.com</span>
  </div>
</section>

</body>
</html>
```